Business Card Design

Velvet Pixel Promotions

An online marketing consulting & strategy business for the cosmetic niche

We specialise in Increasing Leads, Conversions & Content Marketing

I am looking for a very clean, BOLD business card that is simple & effective

Target Market(s)

cosmetic surgeons & cosmetic clinics

Industry/Entity Type

Marketing

Contact Information for Business Card

Darren Okoye
Online Marketing Strategist

Darren@VelvetPixelPromotions.example
0491 268 517

LinkedIn: in/darrenokoye

```html
<!DOCTYPE html>
<html lang="en">
<head>
<meta charset="utf-8">
<title>Velvet Pixel Promotions – Business Card</title>
<link rel="stylesheet" href="https://fonts.googleapis.com/css2?family=Questrial&display=swap">
<style>
  :root {
    --backdrop: #2a2a2c;
    --card-white: #ffffff;
    --card-tint: #f1f1f2;
    --slate: #5d6064;
    --slate-dark: #45484b;
    --sky: #1ba8e6;
    --lime: #8cc63f;
    --ink: #55585c;
    --faint: #d9d2cf;
  }
  * { margin: 0; padding: 0; box-sizing: border-box; }
  html, body {
    width: 1200px; height: 832px; overflow: hidden;
    background: var(--backdrop);
    font-family: "Questrial", "Century Gothic", sans-serif;
  }
  .sheet {
    position: relative; width: 1200px; height: 832px;
    display: flex; align-items: center; justify-content: center; gap: 50px;
  }
  .card {
    position: relative; width: 520px; height: 297px;
    overflow: hidden; background: var(--card-white);
    box-shadow: 0 10px 30px rgba(0,0,0,.45);
  }
  .card-shape { position: absolute; inset: 0; }

  /* back: contact side */
  .brand-small {
    position: absolute; left: 26px; top: 24px;
    display: flex; align-items: center; gap: 10px;
  }
  .brand-dot { width: 30px; height: 30px; border-radius: 50%; background: var(--sky); }
  .brand-small .brand-name {
    color: var(--ink); font-size: 15px; line-height: 1.05;
    letter-spacing: 2px; text-transform: uppercase;
  }
  .contact-list {
    position: absolute; left: 26px; top: 150px; list-style: none;
    color: var(--ink); font-size: 12.5px;
  }
  .contact-list li { display: flex; align-items: center; gap: 8px; height: 19px; }
  .contact-list svg { width: 12px; height: 12px; flex: none; }
  .person {
    position: absolute; right: 26px; top: 196px; text-align: right;
  }
  .person-name { color: var(--sky); font-size: 19px; }
  .person-role { color: var(--lime); font-size: 11.5px; margin-top: 3px; }

  /* front: brand side */
  .brand-large {
    position: absolute; left: 150px; top: 98px;
    display: flex; align-items: center; gap: 16px;
  }
  .brand-large .brand-dot { width: 62px; height: 62px; }
  .brand-large .brand-name {
    color: var(--slate); font-size: 31px; line-height: 1.02;
    letter-spacing: 5px; text-transform: uppercase;
  }
</style>
</head>
<body>
<main class="sheet">

  <section class="card card-back" aria-label="Business card, contact side">
    <svg class="card-shape" viewBox="0 0 520 297" aria-hidden="true">
      <rect width="520" height="297" fill="var(--card-tint)"/>
      <circle cx="215" cy="205" r="92" fill="none" stroke="var(--faint)" stroke-width="26"/>
      <circle cx="520" cy="330" r="242" fill="var(--sky)"/>
      <circle cx="527" cy="336" r="236" fill="var(--card-white)"/>
    </svg>

    <div class="brand-small">
      <span class="brand-dot"></span>
      <span class="brand-name">Velvet<br>Pixel<br>Promotions</span>
    </div>

    <ul class="contact-list">
      <li>
        <svg viewBox="0 0 12 12"><circle cx="6" cy="6" r="6" fill="var(--ink)"/></svg>
        in/darrenokoye
      </li>
      <li>
        <svg viewBox="0 0 12 12"><path d="M1 4c0-2 2-3 5-3s5 1 5 3l-2 1-1-1H4L3 5 1 4zM2.5 6h7l1 5h-9z" fill="var(--ink)"/></svg>
        0491 268 517
      </li>
      <li>
        <svg viewBox="0 0 12 12"><rect x="0.5" y="2" width="11" height="8" fill="var(--ink)"/><path d="M0.5 2.5L6 7l5.5-4.5" fill="none" stroke="#fff" stroke-width="1"/></svg>
        Darren@VelvetPixelPromotions.example
      </li>
    </ul>

    <div class="person">
      <p class="person-name">Darren Okoye</p>
      <p class="person-role">Online Marketing Strategist</p>
    </div>
  </section>

  <section class="card card-front" aria-label="Business card, brand side">
    <svg class="card-shape" viewBox="0 0 520 297" aria-hidden="true">
      <defs>
        <linearGradient id="slate-fade" x1="0" y1="0" x2="1" y2="1">
          <stop offset="0" stop-color="var(--slate-dark)"/>
          <stop offset="1" stop-color="var(--slate)"/>
        </linearGradient>
      </defs>
      <rect width="520" height="297" fill="url(#slate-fade)"/>
      <circle cx="360" cy="215" r="292" fill="var(--sky)"/>
      <circle cx="368" cy="222" r="286" fill="var(--card-white)"/>
    </svg>

    <div class="brand-large">
      <span class="brand-dot"></span>
      <span class="brand-name">Velvet<br>Pixel<br>Promotions</span>
    </div>
  </section>

</main>
</body>
</html>
```